Training course diagram/design

A graphic/diagram for our website and brochures.

We are a training provider and run courses for people who wish to become professionally qualified clinical hypnotherapists.

The graphic needs to illustrate how our training course works at a glance. The training course is comprised of 5 x 4-day classroom based modules and one extra (6th) theory module which is distance learning. The diploma training is a 'rolling' course, so students can join at the beginning of any of the five (classroom) modules. It is important that it is clear from the image that there is not any specific order in which people must attend the modules (the modules have equal status). Attendance of all five modules (and completion of the theory module) will lead to the BQT (Brightmoor Trance Institute) Practitioner Diploma in Clinical Hypnotherapy Diploma.

The names of the classroom modules are:
Medical Hypnosis
Ericksonian Hypnosis
Hypno-psychotherapy
Solution Focused Hypnotherapy
Changework - NLP & Coaching

The 6th (theory module) is called:
The foundations of Hypnotherapy

I have uploaded our logo so you can see our colours/style. Our strapline is:
Practice-ready therapy training
Updates

Please use fonts used in the training school logo: 'Magmawave Caps Bold' and 'Avant Garde Bold'.

Target Market(s)

People who are wanting a creer change

Industry/Entity Type

Hypnotherapy

Font styles to use
Sans Serif
Other font styles liked:
• 'Magmawave Caps Bold' and 'Avant Garde Bold'.

Requirements
Must have
• an individual 'device' or symbol for each module (e.g. colour, shape, etc for each module) so that these can be used on different website pages or in literature where there might be a description of the contents of that module. Fonts that are consistent with branding and are easy to read.
Nice to have
• Something that complements or reflects the training school logo.

```html
<!DOCTYPE html>
<html lang="en">
<head>
<meta charset="utf-8">
<title>Hypnotherapy Practitioner Diploma in Clinical Hypnosis</title>
<link rel="stylesheet" href="https://fonts.googleapis.com/css2?family=Montserrat:wght@600;700&display=swap">
<style>
  :root {
    --olive: #b7c166;
    --teal: #269c89;
    --forest: #0c6858;
    --ink: #0f6a5a;
    --white: #ffffff;
    --mist-deep: #c9d1d4;
    --font: "Montserrat", "Helvetica Neue", Arial, sans-serif;
  }
  * { box-sizing: border-box; margin: 0; padding: 0; }
  html, body { width: 1018px; height: 1200px; overflow: hidden; background: var(--white); }
  .canvas {
    position: relative; width: 1018px; height: 1200px; overflow: hidden;
    font-family: var(--font);
    background: radial-gradient(circle at 50% 50%, #f6f7f7 0%, #e6eaeb 55%, #cfd6d8 100%);
  }
  .title-band {
    position: absolute; left: 0; top: 0; width: 100%; height: 153px;
    background: var(--olive);
    display: flex; align-items: center; justify-content: center; text-align: center;
  }
  .title-band h1 {
    color: var(--white); font-weight: 700; font-size: 42px; line-height: 53px;
  }
  .format-strip {
    position: absolute; left: 0; top: 153px; width: 100%; height: 64px;
    background: linear-gradient(90deg, #ffffff 0%, #e9eced 50%, #c8d0d3 100%);
    display: flex; align-items: center; justify-content: space-between; padding: 0 46px 0 18px;
    color: var(--ink); font-weight: 700; font-size: 27px;
  }
  .module-wheel { position: absolute; left: 0; top: 0; width: 1018px; height: 1200px; }
  .module-label {
    position: absolute; transform: translate(-50%, -50%); text-align: center;
    color: var(--white); font-weight: 700; font-size: 20px; line-height: 29px; white-space: nowrap;
  }
  .module-label.is-online { color: var(--ink); }
  .wheel-centre {
    position: absolute; left: 503px; top: 602px; transform: translate(-50%, -50%);
    text-align: center; color: var(--ink); font-weight: 700; font-size: 33px; line-height: 42px;
  }
  .award-band {
    position: absolute; left: 0; top: 988px; width: 100%; height: 185px;
    background: linear-gradient(90deg, #ffffff 0%, #eef0f1 45%, #c3ccd0 100%);
  }
  .award-icon { position: absolute; left: 58px; top: 10px; width: 135px; height: 162px; }
  .award-title {
    position: absolute; left: 200px; right: 40px; top: 38px; text-align: center;
    color: var(--ink); font-weight: 700; font-size: 30px; line-height: 44px;
  }
  .base-strip { position: absolute; left: 0; top: 1173px; width: 100%; height: 27px; background: var(--mist-deep); }
</style>
</head>
<body>
<div class="canvas">

  <header class="title-band">
    <h1>Hypnotherapy Practitioner Diploma in<br>Clinical Hypnosis</h1>
  </header>

  <div class="format-strip">
    <span class="format-classroom">5 x 4-day classroom modules</span>
    <span class="format-online">1 x online theory module</span>
  </div>

  <svg class="module-wheel" viewBox="0 0 998 1177" aria-hidden="true">
    <defs>
      <filter id="blade-shadow" x="-20%" y="-20%" width="140%" height="140%">
        <feDropShadow dx="2" dy="4" stdDeviation="6" flood-color="#3a4a48" flood-opacity="0.28"/>
      </filter>
      <path id="blade" d="M-131 -319.2 A345 345 0 0 1 200.4 -280.8 L-5.6 -161.9 A162 162 0 0 0 -131 -95.3 Z"/>
    </defs>
    <g transform="translate(495 598)">
      <g filter="url(#blade-shadow)">
        <use href="#blade" class="blade-foundations" fill="#ffffff"/>
        <use href="#blade" class="blade-solution" fill="#b7c166" transform="rotate(60)"/>
        <use href="#blade" class="blade-ericksonian" fill="#269c89" transform="rotate(120)"/>
        <use href="#blade" class="blade-changework" fill="#0c6858" transform="rotate(180)"/>
        <use href="#blade" class="blade-psychotherapy" fill="#b7c166" transform="rotate(240)"/>
        <use href="#blade" class="blade-medical" fill="#269c89" transform="rotate(300)"/>
      </g>
      <g class="online-icon" transform="translate(-75 -193)">
        <circle r="34" fill="#0c6858"/>
        <rect x="-14" y="-13" width="28" height="20" rx="2" fill="none" stroke="#ffffff" stroke-width="3"/>
        <path d="M-20 11 H20" stroke="#ffffff" stroke-width="3.5" stroke-linecap="round"/>
      </g>
    </g>
  </svg>

  <div class="module-label is-online" style="left:490px; top:316px;">The<br>foundations of<br>Hypnotherapy</div>
  <div class="module-label" style="left:726px; top:449px;">Solution<br>Focused<br>Hypnotherapy</div>
  <div class="module-label" style="left:743px; top:685px;">Ericksonian<br>Hypnosis</div>
  <div class="module-label" style="left:515px; top:862px;">Changework -<br>NLP &amp; Coaching</div>
  <div class="module-label" style="left:323px; top:742px;">Hypno-<br>psychotherapy</div>
  <div class="module-label" style="left:270px; top:464px;">Medical<br>Hypnosis</div>

  <div class="wheel-centre">Hypnotherapy<br>Practitioner<br>Diploma</div>

  <footer class="award-band">
    <svg class="award-icon" viewBox="0 0 135 162" aria-hidden="true">
      <path d="M6 6 H96 L129 39 V150 H6 Z" fill="none" stroke="#0c6858" stroke-width="11" stroke-linejoin="round"/>
      <path d="M92 6 V43 H129" fill="none" stroke="#0c6858" stroke-width="9"/>
      <rect x="26" y="38" width="50" height="11" fill="#0c6858"/>
      <rect x="26" y="62" width="80" height="11" fill="#0c6858"/>
      <rect x="26" y="86" width="80" height="11" fill="#0c6858"/>
      <path d="M27 122 V160 L40 150 L53 160 V122 Z" fill="#0c6858" stroke="#ffffff" stroke-width="3"/>
      <circle cx="40" cy="118" r="20" fill="#0c6858" stroke="#ffffff" stroke-width="4"/>
      <circle cx="40" cy="118" r="9" fill="none" stroke="#ffffff" stroke-width="3"/>
    </svg>
    <p class="award-title">BQT (Brightmoor Trance Institute)<br>Practitioner Diploma in Clinical Hypnotherapy</p>
  </footer>

  <div class="base-strip"></div>
</div>
</body>
</html>
```